****Business Card Design for Cormwell Development. Design based around attached logo/company name

I’m looking for business card design for my company Cormwell Development Group,LLC. Design should be professional, sharp and minimal. Outside of the attached logos, greyscale colors for remainder of cards. My thoughts are two-sided card with attached logo on one side and my info on the other but open to one-sided as well with right design.
Target Market(s)
Real estate professionals including banks, private investors, property owners, developers, commercial tenants like Brewlantic, Granvey or Tamsett’s.
Industry/Entity Type
Commercial real estate development and investments.
Contact Information for Business Card
Name, title, email, phone #’s, web address and physical address
Font styles to use
Other font styles liked:
- Helvetica, Garamond, etc
Colors
Designer to choose only greyscale colors for use in the design.
Requirements
Must have
- Attached logo first or second options.
Nice to have
- Two sided card with logo on one side. Attached Logo/company name can be laid out any way that flows as long as it’s legible.name
Should not have
- No loud colors. ***Please do not include logo, I have removed the company design with a logo image.

```html
<!DOCTYPE html>
<html lang="en">
<head>
<meta charset="utf-8">
<title>Cormwell Development Group, LLC — Business Card</title>
<link href="https://fonts.googleapis.com/css2?family=EB+Garamond:wght@400;600&display=swap" rel="stylesheet">
<style>
  :root {
    --backdrop: #c9cacd;
    --paper: #f7f7f6;
    --ink: #4a5163;
    --ink-soft: #5d6476;
    --slate: #444c5f;
    --silver: #d9dbe0;
  }
  * { box-sizing: border-box; margin: 0; padding: 0; }
  html, body {
    width: 1200px;
    height: 1050px;
    overflow: hidden;
    background: var(--backdrop);
    font-family: "EB Garamond", Garamond, serif;
  }
  .canvas {
    position: relative;
    width: 1200px;
    height: 1050px;
  }
  .card {
    position: absolute;
    left: 250px;
    width: 700px;
    height: 400px;
    box-shadow: 0 18px 40px rgba(40, 44, 56, 0.22);
  }
  /* Front: contact side */
  .card--front {
    top: 90px;
    background: var(--paper);
    color: var(--ink);
  }
  .contact {
    position: absolute;
    left: 56px;
    top: 150px;
  }
  .contact__name {
    font-size: 25px;
    font-weight: 400;
    letter-spacing: 1.5px;
    line-height: 1;
  }
  .contact__title {
    font-size: 15px;
    font-weight: 600;
    margin-top: 4px;
  }
  .contact__address {
    font-size: 16px;
    line-height: 1.3;
    margin-top: 16px;
    color: var(--ink-soft);
  }
  .contact__lines {
    display: flex;
    margin-top: 14px;
    font-size: 16px;
    line-height: 1.35;
    color: var(--ink-soft);
  }
  .contact__col { padding-right: 16px; }
  .contact__col + .contact__col {
    padding-left: 16px;
    border-left: 1px solid var(--ink-soft);
  }
  .contact__label { font-weight: 600; margin-right: 6px; }
  .brand-mark {
    position: absolute;
    right: 70px;
    top: 150px;
    display: flex;
    align-items: center;
    gap: 12px;
    font-size: 30px;
    font-weight: 400;
    letter-spacing: 2px;
    color: var(--ink);
  }
  .brand-mark__dot {
    width: 16px;
    height: 16px;
    border-radius: 50%;
    background: var(--ink);
  }
  /* Back: brand side */
  .card--back {
    top: 560px;
    background: var(--slate);
    color: var(--silver);
    display: flex;
    align-items: center;
    justify-content: center;
  }
  .brand-lockup {
    display: flex;
    align-items: center;
    gap: 22px;
  }
  .brand-lockup__dot {
    width: 34px;
    height: 34px;
    border-radius: 50%;
    background: var(--silver);
  }
  .brand-lockup__name {
    font-size: 44px;
    font-weight: 400;
    letter-spacing: 2px;
    line-height: 1.05;
    text-transform: uppercase;
  }
  .brand-lockup__sub {
    display: block;
    font-size: 24px;
    letter-spacing: 3px;
  }
</style>
</head>
<body>
<main class="canvas">
  <section class="card card--front">
    <div class="contact">
      <h1 class="contact__name">DANIEL HARROW</h1>
      <p class="contact__title">President</p>
      <p class="contact__address">4120 Alderwood Lane<br>Fairbanks, Alaska 99701</p>
      <div class="contact__lines">
        <div class="contact__col">
          <div><span class="contact__label">P :</span>555-214-7390</div>
          <div><span class="contact__label">F :</span>555-214-7391</div>
        </div>
        <div class="contact__col">
          <div><span class="contact__label">E :</span>name@cormwelldev.com</div>
          <div><span class="contact__label">W :</span>www.cormwelldev.com</div>
        </div>
      </div>
    </div>
    <div class="brand-mark">
      <span class="brand-mark__dot"></span>
      <span>Cormwell</span>
    </div>
  </section>

  <section class="card card--back">
    <div class="brand-lockup">
      <span class="brand-lockup__dot"></span>
      <p class="brand-lockup__name">Cormwell<span class="brand-lockup__sub">Development Group, LLC</span></p>
    </div>
  </section>
</main>
</body>
</html>
```